high end contractor

high end contracting company we do all phases of construction kitchen,bathrooms,etc... please look at my website before you design www.harborkeybuild.com

would love some sort of lines or logo or both

Industry/Entity Type

Construction

Contact Information for Business Card

company name: oak & meridian contracting address: 318 fenwick st mount Vernon ny 10552 email: harborkeybuild@mailbrook.com website: www.harborkeybuild.com office#: 914-208-3916 fax#: 914-208-5523 dominic valtersen mobile# 917-526-0389

```html
<!DOCTYPE html>
<html lang="en">
<head>
<meta charset="utf-8">
<title>Oak &amp; Meridian Contracting – Business Card</title>
<link rel="stylesheet" href="https://fonts.googleapis.com/css2?family=Arimo:wght@400;700&family=Open+Sans:wght@400;600&display=swap">
<style>
  :root {
    --card-black: #000000;
    --band-grey: #141414;
    --accent-teal: #4bbfbf;
    --text-white: #ffffff;
    --text-soft: #d9d9d9;
  }
  html, body {
    margin: 0;
    padding: 0;
    width: 1200px;
    height: 702px;
    overflow: hidden;
    background: var(--card-black);
  }
  .card {
    position: relative;
    width: 1200px;
    height: 702px;
    background: var(--card-black);
    overflow: hidden;
  }
  .band {
    position: absolute;
    left: 0;
    width: 1200px;
    height: 57px;
    background: var(--band-grey);
  }
  .rule {
    position: absolute;
    width: 3px;
    background: var(--accent-teal);
  }
  .rule--brand { left: 267px; top: 292px; height: 117px; }
  .rule--contact { left: 687px; top: 526px; height: 118px; }
  .brand-name {
    position: absolute;
    left: 281px;
    top: 330px;
    margin: 0;
    font-family: "Arimo", Arial, sans-serif;
    font-size: 36px;
    line-height: 44px;
    letter-spacing: 0.3px;
    color: var(--text-white);
    font-weight: 400;
    white-space: nowrap;
  }
  .brand-name__lead {
    color: var(--accent-teal);
    font-weight: 700;
  }
  .office-details {
    position: absolute;
    right: 540px;
    top: 496px;
    margin: 0;
    padding: 0;
    list-style: none;
    font-family: "Open Sans", Arial, sans-serif;
    font-size: 19px;
    line-height: 29px;
    color: var(--text-soft);
    text-align: right;
    white-space: nowrap;
  }
  .office-details__label {
    color: var(--accent-teal);
    font-weight: 600;
    margin-right: 6px;
  }
  .contact-name {
    position: absolute;
    left: 731px;
    top: 530px;
    margin: 0;
    font-family: "Open Sans", Arial, sans-serif;
    font-size: 39px;
    line-height: 50px;
    color: var(--text-white);
    font-weight: 400;
    white-space: nowrap;
  }
  .contact-mobile {
    position: absolute;
    left: 725px;
    top: 594px;
    display: flex;
    align-items: center;
    font-family: "Open Sans", Arial, sans-serif;
    font-size: 33px;
    color: var(--text-white);
    white-space: nowrap;
  }
  .contact-mobile__badge {
    display: block;
    margin-right: 31px;
  }
</style>
</head>
<body>
  <main class="card">
    <div class="band" style="top:50px"></div>
    <div class="band" style="top:157px"></div>
    <div class="band" style="top:264px"></div>
    <div class="band" style="top:371px"></div>
    <div class="band" style="top:478px"></div>
    <div class="band" style="top:585px"></div>

    <div class="rule rule--brand"></div>
    <h1 class="brand-name"><span class="brand-name__lead">OAK &amp; MERIDIAN</span> CONTRACTING</h1>

    <ul class="office-details">
      <li>318 Fenwick St, Mount Vernon, NY 10552</li>
      <li><span class="office-details__label">O</span>914-208-3916 &nbsp; <span class="office-details__label">F</span>914-208-5523</li>
      <li>harborkeybuild@mailbrook.com</li>
      <li>www.harborkeybuild.com</li>
    </ul>

    <div class="rule rule--contact"></div>
    <p class="contact-name">Dominic Valtersen</p>
    <div class="contact-mobile">
      <svg class="contact-mobile__badge" width="44" height="44" viewBox="0 0 44 44" aria-label="Mobile">
        <circle cx="22" cy="22" r="22" fill="var(--accent-teal)"/>
        <text x="22" y="31" text-anchor="middle" font-family="Open Sans, Arial, sans-serif" font-size="26" font-weight="600" fill="#ffffff">M</text>
      </svg>
      <span class="contact-mobile__number">917-526-0389</span>
    </div>
  </main>
</body>
</html>
```